Business card

We are looking for a creative person to deigns our company business card.

Target Market(s)

College age student

Industry/Entity Type

Accommodation

Contact Information for Business Card

We want a fun, clean and sophisticated design. It should look good, but more importantly the information should be legible.

Font styles to use
Serif
Sans Serif
Other font styles liked:
• Open Sans ,

Colors
33a6d7

Requirements
Must have
• Must have a young and memorable message. Be legible.
• Our logo on the back on a solid blue , please find color and logo attached
• LodgeNestly.com on the back.
Nice to have
• I would like to have couple of different fonts on the LodgeNestly.com on the back of the cards with a solid blue.

```html
<!DOCTYPE html>
<html lang="en">
<head>
<meta charset="utf-8">
<title>LodgeNestly business card</title>
<link href="https://fonts.googleapis.com/css2?family=Arimo:wght@400;700&display=swap" rel="stylesheet">
<style>
  :root {
    --backdrop: #2a2a2c;
    --card: #1b1b1d;
    --blue: #33a6d7;
    --blue-deep: #1d6fa5;
    --icon-ink: #1b1b1d;
  }
  * { margin: 0; padding: 0; box-sizing: border-box; }
  html, body {
    width: 1200px;
    height: 1189px;
    overflow: hidden;
    background: var(--backdrop);
    font-family: "Arimo", Arial, sans-serif;
  }
  .canvas { position: relative; width: 1200px; height: 1189px; }
  .card {
    position: absolute;
    width: 820px;
    height: 470px;
    background: var(--card);
    border-radius: 34px;
    overflow: hidden;
    box-shadow: 0 18px 40px rgba(0,0,0,0.45);
  }
  .card-front { left: 90px; top: 80px; }
  .card-back  { left: 290px; top: 640px; }

  /* Front */
  .front-brand {
    position: absolute;
    left: 0; right: 0; top: 170px;
    text-align: center;
    display: flex; align-items: center; justify-content: center; gap: 14px;
  }
  .brand-dot {
    width: 22px; height: 22px; border-radius: 50%;
    background: var(--blue);
  }
  .brand-name {
    font-weight: 700;
    color: var(--blue);
    font-size: 46px;
    letter-spacing: -0.5px;
  }
  .front-url {
    position: absolute;
    left: 0; right: 0; top: 270px;
    text-align: center;
    color: var(--blue);
    font-size: 19px;
    letter-spacing: 3px;
  }

  /* Back */
  .tab {
    position: absolute;
    left: -30px; top: 58px;
    width: 60px; height: 60px; border-radius: 50%;
    background: var(--blue);
  }
  .person { position: absolute; left: 70px; top: 58px; }
  .person-name {
    color: var(--blue-deep);
    font-weight: 700;
    font-size: 27px;
    letter-spacing: 0.5px;
    line-height: 1;
  }
  .person-role {
    color: var(--blue);
    font-size: 23px;
    line-height: 1.1;
    margin-top: 3px;
  }
  .address {
    position: absolute; left: 80px; top: 182px;
    color: var(--blue);
    font-size: 24px;
    line-height: 1.25;
  }
  .contacts {
    position: absolute; left: 80px; top: 290px;
    list-style: none;
  }
  .contacts li {
    display: flex; align-items: center; gap: 14px;
    color: var(--blue);
    font-size: 24px;
    line-height: 1;
    height: 38px;
  }
  .contacts svg { width: 28px; height: 28px; flex: none; }
  .back-brand {
    position: absolute; right: 60px; top: 196px;
    display: flex; align-items: center; gap: 14px;
  }
  .back-brand .brand-name { font-size: 44px; color: var(--blue); }
</style>
</head>
<body>
<main class="canvas">

  <section class="card card-front" aria-label="Card front">
    <div class="front-brand">
      <span class="brand-dot"></span>
      <span class="brand-name">LodgeNestly</span>
    </div>
    <p class="front-url">www.lodgenestly.com</p>
  </section>

  <section class="card card-back" aria-label="Card back">
    <span class="tab"></span>
    <div class="person">
      <p class="person-name">MARA ELLISON</p>
      <p class="person-role">CEO</p>
    </div>
    <p class="address">PO BOX 48 Harbour Lane<br>7th street Northfield</p>
    <ul class="contacts">
      <li>
        <svg viewBox="0 0 28 28" aria-hidden="true">
          <circle cx="14" cy="14" r="14" fill="#33a6d7"/>
          <rect x="9.5" y="6.5" width="9" height="15" rx="1.5" fill="none" stroke="#1b1b1d" stroke-width="1.8"/>
          <circle cx="14" cy="18.5" r="1" fill="#1b1b1d"/>
        </svg>
        555 014 2786
      </li>
      <li>
        <svg viewBox="0 0 28 28" aria-hidden="true">
          <circle cx="14" cy="14" r="14" fill="#33a6d7"/>
          <rect x="7" y="9" width="14" height="10" fill="none" stroke="#1b1b1d" stroke-width="1.8"/>
          <path d="M7 9 L14 15 L21 9" fill="none" stroke="#1b1b1d" stroke-width="1.8"/>
        </svg>
        hello@lodgenestly.com
      </li>
      <li>
        <svg viewBox="0 0 28 28" aria-hidden="true">
          <circle cx="14" cy="14" r="14" fill="#33a6d7"/>
          <circle cx="14" cy="14" r="7.5" fill="none" stroke="#1b1b1d" stroke-width="1.6"/>
          <ellipse cx="14" cy="14" rx="3.2" ry="7.5" fill="none" stroke="#1b1b1d" stroke-width="1.4"/>
          <path d="M6.5 14 H21.5 M8 10 H20 M8 18 H20" stroke="#1b1b1d" stroke-width="1.3"/>
        </svg>
        www.lodgenestly.com
      </li>
    </ul>
    <div class="back-brand">
      <span class="brand-dot"></span>
      <span class="brand-name">LodgeNestly</span>
    </div>
  </section>

</main>
</body>
</html>
```